New Business Card Design For Re-Branded Company (New Logo)

We recently switched our DBA and had a new logo designed. We now need new business cards made around our new logo. We would like to stick with the color scheme in our logo: White, Orange, and Blue. We want to see original bold designs that reflect our position in the solar energy sector but we prefer simple over complicated.

We are curious about vertical designs so if you can translate your design onto a vertical layout we would be open to look at it. We especially like a few designs we have seen on here that are vertical with a black or very dark gray background. They have our logo on one side and then the normal vertical business card on the other side.

I have included a screenshot of one of the samples we like, labeled sample.jpg and a file we were given as an example of our logo on a dark background.

At the same time we are satisfied to stay with what we have always had in a horizontal format. If it's not a lot of extra work for you, designs that are submitted in both horizontal and vertical formats will be greatly appreciated.

Please submit your original, bold, clean designs for consideration. Contact us with any questions or comments that may arise.

Thank you and Good Luck,

KP

```html
<!DOCTYPE html>
<html lang="en">
<head>
<meta charset="utf-8">
<title>Kestrel Power – Business Card</title>
<link rel="stylesheet" href="https://fonts.googleapis.com/css2?family=Montserrat:wght@400;700&family=Open+Sans:wght@400;600&display=swap">
<style>
  :root {
    --backdrop: #e9e6e1;
    --card: #3f4042;
    --card-edge: #2e2f31;
    --orange: #f39a1f;
    --orange-deep: #e6801a;
    --blue: #1996d3;
    --white: #ffffff;
    --muted: #e4e4e4;
  }
  * { box-sizing: border-box; margin: 0; padding: 0; }
  html, body { width: 1200px; height: 780px; overflow: hidden; }
  body {
    background: var(--backdrop);
    display: flex;
    align-items: center;
    justify-content: center;
    gap: 110px;
    font-family: "Open Sans", Arial, sans-serif;
  }
  .card {
    position: relative;
    width: 330px;
    height: 560px;
    border-radius: 18px;
    background: linear-gradient(160deg, #4a4b4d 0%, var(--card) 45%, var(--card-edge) 100%);
    overflow: hidden;
    box-shadow: 0 10px 28px rgba(0,0,0,.22);
  }
  .card-band {
    position: absolute;
    left: 0; right: 0; bottom: 0;
    height: 84px;
    background: linear-gradient(180deg, var(--orange) 0%, var(--orange-deep) 100%);
    display: flex;
    align-items: center;
    justify-content: center;
  }
  .website {
    font-family: "Montserrat", Arial, sans-serif;
    font-size: 20px;
    color: var(--white);
    letter-spacing: .5px;
  }

  /* Front */
  .brand {
    position: absolute;
    top: 56px; left: 0; right: 0;
    display: flex;
    flex-direction: column;
    align-items: center;
    gap: 16px;
  }
  .brand-dot {
    width: 64px; height: 64px;
    border-radius: 50%;
    border: 5px solid var(--orange);
  }
  .brand-name {
    font-family: "Montserrat", Arial, sans-serif;
    font-weight: 700;
    font-size: 30px;
    letter-spacing: 1px;
    color: var(--orange);
  }
  .person {
    position: absolute;
    top: 222px; left: 0; right: 0;
    text-align: center;
  }
  .person-name {
    font-family: "Montserrat", Arial, sans-serif;
    font-weight: 700;
    font-size: 23px;
    color: var(--orange);
    letter-spacing: 1px;
  }
  .person-title {
    font-size: 19px;
    color: var(--white);
    margin-top: 2px;
  }
  .contact {
    position: absolute;
    top: 318px; left: 0; right: 0;
    text-align: center;
    color: var(--muted);
    font-size: 18px;
    line-height: 26px;
    list-style: none;
  }
  .contact-line {
    display: flex;
    justify-content: center;
    align-items: center;
    gap: 8px;
  }
  .contact-icon {
    width: 20px; height: 20px;
    border-radius: 3px;
    background: var(--orange);
    display: inline-flex;
    align-items: center;
    justify-content: center;
  }

  /* Back */
  .mark {
    position: absolute;
    top: 150px; left: 0; right: 0;
    display: flex;
    flex-direction: column;
    align-items: center;
    gap: 26px;
  }
  .mark-ring {
    width: 170px; height: 170px;
    border-radius: 50%;
    border: 12px solid var(--orange);
  }
  .mark-name {
    font-family: "Montserrat", Arial, sans-serif;
    font-weight: 700;
    font-size: 28px;
    letter-spacing: 1px;
    color: var(--blue);
  }
</style>
</head>
<body>

  <article class="card card-front">
    <header class="brand">
      <span class="brand-dot"></span>
      <span class="brand-name">KESTREL POWER</span>
    </header>

    <section class="person">
      <p class="person-name">EMPLOYEE NAME</p>
      <p class="person-title">Owner</p>
    </section>

    <ul class="contact">
      <li class="contact-line">
        <span class="contact-icon">
          <svg width="14" height="14" viewBox="0 0 24 24" aria-hidden="true"><path fill="#3f4042" d="M6.6 10.8a15.1 15.1 0 0 0 6.6 6.6l2.2-2.2a1 1 0 0 1 1-.25 11.4 11.4 0 0 0 3.6.57 1 1 0 0 1 1 1V20a1 1 0 0 1-1 1A17 17 0 0 1 3 4a1 1 0 0 1 1-1h3.5a1 1 0 0 1 1 1c0 1.25.2 2.45.57 3.57a1 1 0 0 1-.25 1z"/></svg>
        </span>
        123-456-7890
      </li>
      <li class="contact-line">
        <span class="contact-icon">
          <svg width="14" height="14" viewBox="0 0 24 24" aria-hidden="true"><rect x="3" y="9" width="18" height="10" rx="2" fill="#3f4042"/><rect x="7" y="4" width="10" height="6" fill="#3f4042"/><rect x="7" y="14" width="10" height="2" fill="#f39a1f"/></svg>
        </span>
        123-456-7890
      </li>
      <li class="contact-line">your@yourgmail.com</li>
      <li class="contact-line">1111 youraddress Lane</li>
      <li class="contact-line">Millbrook TX 00000</li>
    </ul>

    <footer class="card-band">
      <span class="website">yourwebsite.com</span>
    </footer>
  </article>

  <article class="card card-back">
    <div class="mark">
      <span class="mark-ring"></span>
      <span class="mark-name">KESTREL POWER</span>
    </div>
    <footer class="card-band">
      <span class="website">yourwebsite.com</span>
    </footer>
  </article>

</body>
</html>
```